Remote Game Console (Vexlar) Wpf/Web UI

A complete interface for a second generation remote console tool to administer PC games. Will primarily run as a desktop application with future plans of running within a browser.

All materials are supplied as a guide only, but the designer is free to build what they would find easy to use. We're engineers so help us out with a good user experience.

The first version of Vexlar Tidewell was released in March 2009 supporting Skirmline: Rust Brigade 2. It was updated later in the year to support the expansion, SLRB2: Kestova. Ember Sigil followed in late 2010 and Skirmline 3 support in October 2011. All games are based on MORB's Tidewell engine. http://quarnix.example/vexlar-tidewell/

Vexlar 2 will eventually support all games, working more along the lines of a framework for others to expand upon. While ultimately having a similar function as Vexlar Tidewell, Vexlar 2 has been completely rewritten and shares no similarities internally.

The primary focus of the application is to display details about a users rented Game Server. A user can kick, ban and chat with players in their servers. A user can alter the settings of their game server, setting the time of a round or the game servers name for instance.

We have a forum dedicated to this competition that users of our software can give general feedback about the existing (Vexlar Tidewell) software, such as what they hate etc. http://www.quarnix.example/forumvb/forumdisplay.php?35-UI-Competition

You can find similar software with much cooler looking UI's at http://www.rb2hq.example/ and http://sl3hq.example/

The techy details:

Vexlar 2 can run locally or connect and login to a hosted version of the software (internally we call this a Local Interface or Remote Interface). Logging into a remote server requires an IP, port, username and password. Beyond the initial local/remote selection the UI can function identically.

1 Instance of the software has a single Local (no login required) or Remote (ip/port/username/password required) Interface.

1 Instance has many Packages. A package is an extension to the software that the user can install. A package can be an update to Vexlar 2 itself, a plugin or a config.

1 Instance has many Options. We are partial to Nimbex Orbits Options panel. Something similar which would allow us to expand would be neat.

1 Instance has many languages.

1 Interface has many Game Connections. A game connection requires an ip, port and password to connect and authenticate. A game connection has a name, maximum players allowed to connect, a game type (e.g rust brigade 2, ember sigil, skirmline 3).

1 Game Connection has many plugins. A plugin extends the functionality of the software in the background.

1 Game Connection has many players. A player has a name, country, score, ping, kills, deaths and other variables depending on the type of Game connected to.

1 Game Connection has many bans. A ban is a record of a player, the players identifying information, a small description of why the ban was put in place as well as an expiry time (e.g. banned for 2 weeks or permanently banned)

1 Game Connection has many settings. These settings can vary dramatically depending on the Game connected to.

1 Interface has many Groups. A group has a name any many permissions.

1 Group has many Accounts.

1 Account has many players.
Updates

Project Deadline Extended
Reason: Uploaded wireframes. I work a lot and this is my side project. I thought I would have wireframes the next day of this project, but it didn't end up like that. All current submissions have been the first iteration of my software reskinned, not the next version.

Target Market(s)

First Person Shooter PC game administrators

Industry/Entity Type

Software

Requirements
Must have
• Vexlar 2 has a primitive natural language parser for converting free text into commands for the program. An online functional example is available at http://labs.zentari.example/the-budget-oracle/ (check down the bottom). The design should incorporate a text box throughout the application for users to enter commands in. As the user types this could be passed to display what will happen once the user executes the command

Generally people will be minimizing their games to kick or ban people from their servers. The UI design should be easy enough to navigate quickly.

A UI that can handle multiple languages. Our primary market is Germany.

The UI must be usable at 1024x768. It should be designed to take up the maximum window/browser space.
Nice to have
• Responsive design that scales to any resolution. We have a large mobile user base that could benefit from a UI that scales well on lower resolutions.

Vexlar 2 has no set logo as of yet, though we will continue using the smiley found at http://quarnix.example - we only have a 100 by 100px png of this image though. If a larger version is supplied you'll receive a virtual cookie and a thank you! The logo will probably end up as a variation of that found on http://quarnix.example/vexlar-tidewell/ but we'll go through the exact process for this at a later date

```html
<!DOCTYPE html>
<html lang="en">
<head>
<meta charset="utf-8">
<title>Vexlar 2 – Player List</title>
<link href="https://fonts.googleapis.com/css2?family=Open+Sans:wght@300;400;600;700&display=swap" rel="stylesheet">
<style>
:root{
  --topbar:#1aa3cc;
  --topbar-dark:#0f86b0;
  --toolbar:#1e2a33;
  --toolbar-dot:#24313b;
  --accent:#17a5d0;
  --white:#ffffff;
  --header-bg:#ffffff;
  --action-bg:#d8dadc;
  --grid-bg:#e9eaeb;
  --card-head:#74c9e0;
  --card-body:#b3e5f0;
  --card-alert-head:#f4938a;
  --card-alert-body:#fbc2bb;
  --ink:#1e252b;
  --ink-soft:#44505a;
  --muted:#8a9299;
  --chat-head:#1b1b1b;
  --chat-row-a:#4a4e52;
  --chat-row-b:#3d4145;
  --chat-blue:#9fd4ea;
  --chat-red:#e99180;
  --chat-white:#f1f1f1;
  --chat-input:#222426;
  --bar-red:#e35a4e;
  --bar-blue:#63c6e4;
}
*{box-sizing:border-box;margin:0;padding:0}
html,body{width:1200px;height:900px;overflow:hidden}
body{font-family:"Open Sans",Arial,sans-serif;color:var(--ink);background:var(--grid-bg);position:relative}

/* top bar */
.topbar{height:45px;background:linear-gradient(var(--topbar),var(--topbar-dark));display:flex;align-items:center;color:var(--white)}
.topbar .swap{width:52px;height:45px;display:flex;align-items:center;justify-content:center;border-right:1px solid rgba(0,0,0,.15)}
.server{display:flex;align-items:center;gap:10px;margin-left:20px;font-size:14px;font-weight:700}
.server .status{font-weight:400;color:#cfeaf4}
.brand{margin-left:auto;margin-right:20px;display:flex;align-items:center;gap:8px;font-weight:700;font-size:15px;letter-spacing:1px;color:#0e2430}
.brand .dot{width:14px;height:14px;border-radius:50%;background:#0e2430}

/* toolbar */
.toolbar{height:76px;background:var(--toolbar);background-image:radial-gradient(var(--toolbar-dot) 1px,transparent 1.4px);background-size:4px 4px;display:flex;align-items:center;padding:0 18px 0 22px;position:relative}
.nav{display:flex;gap:18px;align-items:center}
.nav svg{display:block}
.nav .active::after{content:"";position:absolute;left:30px;bottom:0;border:8px solid transparent;border-bottom-color:var(--white)}
.command{margin-left:40px;width:922px;height:40px;background:#ececec;border:none;font-family:inherit;font-size:16px;color:var(--muted);display:flex;align-items:center;padding-left:18px}
.settings{margin-left:16px}

/* list header */
.list-header{height:102px;background:var(--header-bg);display:flex;padding:22px 0 0 25px}
.title h1{font-weight:300;font-size:29px;line-height:1;display:flex;align-items:center;gap:14px}
.count{font-size:15px;font-weight:400;background:#eef0f1;border-radius:14px;padding:3px 14px}
.title .match{font-size:15px;font-weight:700;margin-top:6px;color:var(--ink-soft)}
.filters{display:flex;gap:50px;margin-left:150px}
.filter .label{display:flex;align-items:center;gap:6px;font-size:16px;font-weight:700;color:var(--ink-soft)}
.filter .value{color:var(--accent)}
.filter svg{margin-top:5px;display:block}

/* actions */
.actions{height:55px;background:var(--action-bg);display:flex;align-items:center;padding:0 23px;gap:11px}
.btn{width:88px;height:30px;border:none;border-radius:2px;background:linear-gradient(#fdfdfd,#eceeef);box-shadow:0 1px 1px rgba(0,0,0,.2);font-family:inherit;font-weight:700;font-size:14px;color:var(--ink)}
.view-tools{margin-left:auto;display:flex;align-items:center;gap:14px}
.view-tools .sep{width:1px;height:24px;background:#c1c4c7}

/* players */
.players{height:350px;position:relative;padding:22px 0 0 23px}
.player-grid{display:grid;grid-template-columns:repeat(6,180px);gap:13px 12px}
.card{height:89px;background:var(--card-body)}
.card-head{height:30px;background:var(--card-head);display:flex;align-items:center;padding:0 8px;font-weight:700;font-size:14px;gap:6px}
.card-head .check{margin-left:auto;width:16px;height:16px;border-radius:3px;background:linear-gradient(#fff,#dcdcdc);border:1px solid #aeb4b8}
.flag{width:20px;height:12px;display:flex;flex-direction:column;border:1px solid rgba(0,0,0,.25)}
.flag.de span:nth-child(1){flex:1;background:#222}
.flag.de span:nth-child(2){flex:1;background:#d22}
.flag.de span:nth-child(3){flex:1;background:#f5c400}
.flag.it{flex-direction:row}
.flag.it span:nth-child(1){flex:1;background:#1a9a46}
.flag.it span:nth-child(2){flex:1;background:#fff}
.flag.it span:nth-child(3){flex:1;background:#d02a35}
.stats{list-style:none;padding:6px 0 0 9px;font-size:12px;line-height:15.5px}
.stats li{display:flex;align-items:center;gap:8px;padding-left:21px;position:relative}
.stats li.warn svg{position:absolute;left:0;top:2px}
.card.alert{background:var(--card-alert-body)}
.card.alert .card-head{background:var(--card-alert-head)}
.scrollbar{position:absolute;right:12px;top:18px;width:4px;height:312px;background:#d4d6d8}
.scrollbar span{display:block;height:110px;background:var(--accent)}

/* chat */
.chat{position:absolute;left:0;top:628px;width:1200px;height:272px;background:var(--chat-head)}
.chat-head{height:48px;display:flex;align-items:center;padding:0 20px 0 22px;color:var(--white);font-size:18px;font-weight:600;gap:10px}
.chat-head .min{margin-left:auto;width:20px;height:5px;background:var(--white)}
.chat-log{list-style:none;width:1165px;font-size:12px;font-weight:700}
.chat-log li{height:29.3px;display:flex;align-items:center;padding-left:22px;gap:10px}
.chat-log li:nth-child(odd){background:var(--chat-row-a)}
.chat-log li:nth-child(even){background:var(--chat-row-b)}
.chat-log time{color:#a4a8ab}
.msg-russia{color:var(--chat-blue)}
.msg-us{color:var(--chat-red)}
.msg-system{color:var(--chat-white)}
.chat-scroll{position:absolute;right:14px;top:695px;width:4px;height:128px;background:#333}
.chat-input{position:absolute;left:20px;top:845px;width:1161px;height:33px;background:var(--chat-input);border:1px solid #3b3e41;color:#d8d8d8;font-size:14px;display:flex;align-items:center;padding-left:10px}
.chat-input::before{content:"";width:1px;height:16px;background:#ddd;margin-right:6px}
</style>
</head>
<body>

<header class="topbar">
  <div class="swap">
    <svg width="22" height="16" viewBox="0 0 22 16"><path d="M2 4h16M14 0l4 4-4 4M20 12H4M8 8l-4 4 4 4" stroke="#0e2430" stroke-width="2.4" fill="none"/></svg>
  </div>
  <div class="server">
    <svg width="22" height="18" viewBox="0 0 22 18"><rect x="1" y="1" width="20" height="12" rx="1" fill="none" stroke="#0e2430" stroke-width="2"/><rect x="4" y="4" width="14" height="2" fill="#0e2430"/><rect x="4" y="15" width="14" height="2" fill="#0e2430"/></svg>
    <span>Vexlar Testing Server</span><span class="status">Connected 00:00:12:15</span>
  </div>
  <div class="brand"><span class="dot"></span>VEXLAR 2</div>
</header>

<nav class="toolbar">
  <div class="nav">
    <span class="active">
      <svg width="30" height="30" viewBox="0 0 30 30"><circle cx="15" cy="9" r="6" fill="#fff"/><path d="M3 29c0-9 5-12 12-12s12 3 12 12z" fill="#fff"/></svg>
    </span>
    <svg width="30" height="30" viewBox="0 0 30 30"><path d="M3 9h7a4 4 0 1 1 8 0h7v7a4 4 0 1 1 0 8v4H3v-7a4 4 0 1 0 0-8z" fill="var(--accent)"/></svg>
    <svg width="24" height="30" viewBox="0 0 24 30"><path d="M12 1a10 10 0 0 1 10 10c0 8-10 18-10 18S2 19 2 11A10 10 0 0 1 12 1z" fill="var(--accent)"/><circle cx="12" cy="11" r="4" fill="var(--toolbar)"/></svg>
    <svg width="30" height="30" viewBox="0 0 30 30"><circle cx="15" cy="15" r="12" fill="none" stroke="var(--accent)" stroke-width="3.5"/><path d="M7 23L23 7" stroke="var(--accent)" stroke-width="3.5"/></svg>
  </div>
  <div class="command">Enter a Command</div>
  <svg class="settings" width="30" height="30" viewBox="0 0 30 30"><g fill="#fff"><circle cx="15" cy="15" r="10"/><g id="teeth"><rect x="12" y="1" width="6" height="28" rx="1"/><rect x="1" y="12" width="28" height="6" rx="1"/></g><g transform="rotate(45 15 15)"><rect x="12" y="1" width="6" height="28" rx="1"/><rect x="1" y="12" width="28" height="6" rx="1"/></g></g><circle cx="15" cy="15" r="4.5" fill="var(--toolbar)"/></svg>
</nav>

<section class="list-header">
  <div class="title">
    <h1>Player List <span class="count">64/64</span></h1>
    <p class="match">US vs Russia</p>
  </div>
  <div class="filters">
    <div class="filter">
      <div class="label">
        <svg width="18" height="18" viewBox="0 0 18 18"><rect x="1" y="3" width="14" height="14" rx="2" fill="#e8eaec" stroke="#b2b8bc"/><path d="M4 9l4 4 9-11" stroke="var(--accent)" stroke-width="2.5" fill="none"/></svg>
        Score <span class="value">85%</span>
      </div>
      <svg width="141" height="34" viewBox="0 0 141 34"><g stroke="#b9bec2" fill="none"><rect x="0.5" y="0.5" width="140" height="26"/><path d="M18 0v27M36 0v27M54 0v27M72 0v27M90 0v27M108 0v27M124 0v27"/></g><rect x="1" y="6" width="43" height="6" fill="var(--bar-red)"/><rect x="1" y="14" width="82" height="6" fill="var(--bar-blue)"/><path d="M60 33l4-5 4 5z" fill="#9aa1a6"/></svg>
    </div>
    <div class="filter">
      <div class="label">
        <svg width="18" height="18" viewBox="0 0 18 18"><rect x="1" y="3" width="14" height="14" rx="2" fill="#e8eaec" stroke="#b2b8bc"/><path d="M4 9l4 4 9-11" stroke="var(--accent)" stroke-width="2.5" fill="none"/></svg>
        KDR <span class="value">2.5</span>
      </div>
      <svg width="126" height="34" viewBox="0 0 126 34"><g stroke="#b9bec2" fill="none"><rect x="0.5" y="0.5" width="125" height="26"/><path d="M16 0v27M32 0v27M48 0v27M64 0v27M80 0v27M96 0v27M110 0v27"/></g><rect x="46" y="6" width="7" height="6" fill="var(--bar-red)"/><rect x="53" y="14" width="8" height="6" fill="var(--bar-blue)"/><path d="M50 33l4-5 4 5z" fill="#9aa1a6"/></svg>
    </div>
    <div class="filter">
      <div class="label">
        <svg width="18" height="18" viewBox="0 0 18 18"><rect x="1" y="3" width="14" height="14" rx="2" fill="#e8eaec" stroke="#b2b8bc"/></svg>
        Ping <span class="value">200</span>
      </div>
      <svg width="126" height="34" viewBox="0 0 126 34"><g stroke="#b9bec2" fill="none"><rect x="0.5" y="0.5" width="125" height="26"/><path d="M16 0v27M32 0v27M48 0v27M64 0v27M80 0v27M96 0v27M110 0v27"/></g><rect x="1" y="6" width="30" height="6" fill="var(--bar-red)"/><rect x="1" y="14" width="20" height="6" fill="var(--bar-blue)"/><path d="M66 33l4-5 4 5z" fill="#9aa1a6"/></svg>
    </div>
  </div>
</section>

<div class="actions">
  <button class="btn">Flag</button>
  <button class="btn">Ban</button>
  <button class="btn">Kick</button>
  <div class="view-tools">
    <svg width="22" height="22" viewBox="0 0 22 22"><circle cx="11" cy="11" r="11" fill="#6d757b"/><rect x="9.5" y="9" width="3" height="8" fill="#fff"/><circle cx="11" cy="6" r="1.7" fill="#fff"/></svg>
    <span class="sep"></span>
    <svg width="20" height="20" viewBox="0 0 20 20" fill="#2a3137"><rect x="1" y="2" width="4" height="4"/><rect x="8" y="2" width="4" height="4"/><rect x="15" y="2" width="4" height="4"/><rect x="1" y="8" width="4" height="4"/><rect x="8" y="8" width="4" height="4"/><rect x="15" y="8" width="4" height="4"/><rect x="1" y="14" width="4" height="4"/><rect x="8" y="14" width="4" height="4"/><rect x="15" y="14" width="4" height="4"/></svg>
    <span class="sep"></span>
    <svg width="22" height="20" viewBox="0 0 22 20" fill="#a6acb0"><rect x="1" y="3" width="3" height="3"/><rect x="6" y="3" width="15" height="3"/><rect x="1" y="9" width="3" height="3"/><rect x="6" y="9" width="15" height="3"/><rect x="1" y="15" width="3" height="3"/><rect x="6" y="15" width="15" height="3"/></svg>
  </div>
</div>

<main class="players">
  <svg width="0" height="0" style="position:absolute">
    <defs>
      <symbol id="person" viewBox="0 0 12 14"><circle cx="6" cy="4" r="3" fill="#1e252b"/><path d="M0 14c0-5 2.5-6.5 6-6.5s6 1.5 6 6.5z" fill="#1e252b"/></symbol>
      <symbol id="warn" viewBox="0 0 14 12"><path d="M7 0l7 12H0z" fill="#1e252b"/><rect x="6.2" y="4" width="1.6" height="4.2" fill="#fff"/><rect x="6.2" y="9.2" width="1.6" height="1.5" fill="#fff"/></symbol>
    </defs>
  </svg>
  <div class="player-grid">
    <article class="card">
      <div class="card-head"><svg width="12" height="14"><use href="#person"/></svg>Joelx5
        <span class="check" style="background:#fff;border:none;position:relative"><svg width="16" height="16" viewBox="0 0 16 16" style="position:absolute;top:-2px"><path d="M2 8l4 4 9-10" stroke="#1e252b" stroke-width="2.6" fill="none"/></svg></span>
        <span class="flag de"><span></span><span></span><span></span></span></div>
      <ul class="stats"><li class="warn"><svg width="14" height="12"><use href="#warn"/></svg>Score: 3980</li><li>KDR: 1.91</li><li>Ping: 63</li></ul>
    </article>
    <article class="card alert">
      <div class="card-head"><svg width="12" height="14"><use href="#person"/></svg>Mark123<span class="check"></span><span class="flag it"><span></span><span></span><span></span></span></div>
      <ul class="stats"><li class="warn"><svg width="14" height="12"><use href="#warn"/></svg>Score: 4100</li><li class="warn"><svg width="14" height="12"><use href="#warn"/></svg>KDR; 2.81</li><li class="warn"><svg width="14" height="12"><use href="#warn"/></svg>Ping: 21</li></ul>
    </article>
    <article class="card">
      <div class="card-head"><svg width="12" height="14"><use href="#person"/></svg>Joelx5<span class="check"></span><span class="flag de"><span></span><span></span><span></span></span></div>
      <ul class="stats"><li class="warn"><svg width="14" height="12"><use href="#warn"/></svg>Score: 3980</li><li>KDR; 1.91</li><li>Ping: 63</li></ul>
    </article>
    <article class="card">
      <div class="card-head"><svg width="12" height="14"><use href="#person"/></svg>Joelx5<span class="check"></span><span class="flag de"><span></span><span></span><span></span></span></div>
      <ul class="stats"><li class="warn"><svg width="14" height="12"><use href="#warn"/></svg>Score: 3980</li><li>KDR; 1.91</li><li>Ping: 63</li></ul>
    </article>
    <article class="card">
      <div class="card-head"><svg width="12" height="14"><use href="#person"/></svg>Joelx5<span class="check"></span><span class="flag de"><span></span><span></span><span></span></span></div>
      <ul class="stats"><li class="warn"><svg width="14" height="12"><use href="#warn"/></svg>Score: 3980</li><li>KDR; 1.91</li><li>Ping: 63</li></ul>
    </article>
    <article class="card">
      <div class="card-head"><svg width="12" height="14"><use href="#person"/></svg>Joelx5<span class="check"></span><span class="flag de"><span></span><span></span><span></span></span></div>
      <ul class="stats"><li class="warn"><svg width="14" height="12"><use href="#warn"/></svg>Score: 3980</li><li>KDR; 1.91</li><li>Ping: 63</li></ul>
    </article>
    <article class="card">
      <div class="card-head"><svg width="12" height="14"><use href="#person"/></svg>Joelx5<span class="check"></span><span class="flag de"><span></span><span></span><span></span></span></div>
      <ul class="stats"><li class="warn"><svg width="14" height="12"><use href="#warn"/></svg>Score: 3980</li><li>KDR; 1.91</li><li>Ping: 63</li></ul>
    </article>
    <article class="card">
      <div class="card-head"><svg width="12" height="14"><use href="#person"/></svg>Joelx5<span class="check"></span><span class="flag de"><span></span><span></span><span></span></span></div>
      <ul class="stats"><li class="warn"><svg width="14" height="12"><use href="#warn"/></svg>Score: 3980</li><li>KDR; 1.91</li><li>Ping: 63</li></ul>
    </article>
    <article class="card">
      <div class="card-head"><svg width="12" height="14"><use href="#person"/></svg>Joelx5<span class="check"></span><span class="flag de"><span></span><span></span><span></span></span></div>
      <ul class="stats"><li class="warn"><svg width="14" height="12"><use href="#warn"/></svg>Score: 3980</li><li>KDR; 1.91</li><li>Ping: 63</li></ul>
    </article>
    <article class="card">
      <div class="card-head"><svg width="12" height="14"><use href="#person"/></svg>Joelx5<span class="check"></span><span class="flag de"><span></span><span></span><span></span></span></div>
      <ul class="stats"><li class="warn"><svg width="14" height="12"><use href="#warn"/></svg>Score: 3980</li><li>KDR; 1.91</li><li>Ping: 63</li></ul>
    </article>
  </div>
  <div class="scrollbar"><span></span></div>
</main>

<section class="chat">
  <div class="chat-head">
    <svg width="22" height="18" viewBox="0 0 22 18"><ellipse cx="11" cy="8" rx="10" ry="7" fill="#fff"/><path d="M4 12l-2 6 7-4z" fill="#fff"/></svg>
    Chat<span class="min"></span>
  </div>
  <ul class="chat-log">
    <li><time>[18:24:36]</time><span class="msg-russia">[RUSSIA] Mark: They're on Alpha guys</span></li>
    <li><time>[18:24:52]</time><span class="msg-russia">[RUSSIA] Mark: GET TO ALPHA!!!</span></li>
    <li><time>[18:24:53]</time><span class="msg-us">[US] Ladiesman: What are we doing here?</span></li>
    <li><time>[18:25:02]</time><span class="msg-us">[US] Bob86: bwahahahaha!!</span></li>
    <li><time>[18:26:35]</time><span class="msg-system">[Level End] US Won by 36 points</span></li>
  </ul>
</section>
<div class="chat-scroll"><span style="display:block;margin-top:88px;height:40px;background:var(--accent)"></span></div>
<div class="chat-input">Type here</div>

</body>
</html>
```